Webdesign/Updates

We would like a landing page for an online course for our educators. So a website with about 3 to 5 pages - Home, About US, Online course, blog, and Contact us. We have a wordpress site up using a template, but we are looking for something that connects more with our new logo.

Target Market(s)

Educators, workshop trainers/instructors, colleges, community schools, educational institutions, global organizations

Industry/Entity Type

Education

Contact Information for Business Card

Use the words below as place holders for the front:
Name
Title
Address line 1
Address line 2
Email
Phone
Website URL

--the back
Logo
1 short question, use "What do you 1234 about your program?"

Number of Pages Required

4 page

Requirements
Must have
• Home page
• Course Page
• Blog
• right side bar with social media content and invitation to subscribe to newsletter
• see logo colors in document
Nice to have
• Newsletter Page with graphic that can be on this page or page can be sent as a pdf via email or in an email.
Should not have
• Be better than attached description
• clean simple look but stylish

```html
<!DOCTYPE html>
<html lang="en">
<head>
<meta charset="utf-8">
<title>Blog – Teach Forward</title>
<link href="https://fonts.googleapis.com/css2?family=Montserrat:wght@400;500;600;700&display=swap" rel="stylesheet">
<style>
:root{
  --blue:#1fa3dd;
  --green:#9dc43a;
  --orange:#ef5a2a;
  --ink:#111;
  --body:#333;
  --rule:#d6d6d6;
  --fb:#3b5998;--tw:#45a3ec;--pi:#bd1f2b;--ig:#a3238f;
  --gp:#d0432f;--li:#2d6fb5;--yt:#a5020a;--rss:#e07f0b;
}
*{margin:0;padding:0;box-sizing:border-box}
html,body{width:798px;height:1200px;overflow:hidden;background:#fff}
body{position:relative;font-family:'Montserrat',sans-serif;color:var(--body)}
.abs{position:absolute}

.hero{left:0;top:0;width:798px;height:258px;
  background:linear-gradient(180deg,#e9e8e8 0%,#cfcdcd 55%,#6a6665 80%,#3a3837 100%)}
.site-header{left:0;top:0;width:798px;height:52px;background:rgba(255,255,255,.86)}
.brand{left:156px;top:18px;font-weight:700;font-size:13px;letter-spacing:1.4px;color:var(--blue)}
.main-nav{top:22px;font-size:6.5px;font-weight:600;letter-spacing:.9px;color:#222}
.nav-active{left:491px;top:34px;width:48px;height:2px;
  background:linear-gradient(90deg,var(--blue) 33%,var(--green) 33% 66%,var(--orange) 66%)}
.page-label{left:156px;top:186px;width:74px;height:38px;background:rgba(30,30,30,.85);
  color:#fff;font-weight:700;font-size:13px;line-height:38px;padding-left:22px}
.page-label::before{content:"";position:absolute;left:15px;top:8px;width:2px;height:22px;
  background:linear-gradient(180deg,var(--blue) 33%,var(--green) 33% 66%,var(--orange) 66%)}

.post-title{left:156px;font-weight:700;font-size:14.5px;color:var(--ink);letter-spacing:.3px}
.post-meta{left:156px;font-size:7.5px;color:var(--blue)}
.post-meta span{margin:0 6px;color:#9ab}
.post-image{left:156px;width:324px;height:224px;
  background:linear-gradient(90deg,#f1efec 0%,#e4e1dc 15%,#2b2b2b 18%,#343434 65%,#e7e4df 72%,#6a3a32 82%,#eee 100%)}
.post-excerpt{left:156px;width:324px;font-size:6.4px;line-height:10.8px;color:#333}
.post-links{left:156px;font-size:6.4px;font-weight:700;color:var(--blue)}
.post-rule{left:156px;width:324px;height:1px;background:var(--rule)}

.signup{left:500px;top:330px;width:142px;height:164px;border:1px solid #ddd;border-top:0;border-bottom:0;background:#fff}
.bar{position:absolute;left:0;width:142px;height:7px;
  background:linear-gradient(90deg,var(--blue) 33%,var(--green) 33% 66%,var(--orange) 66%)}
.bar.thin{height:2px}
.signup h3{position:absolute;left:8px;top:25px;width:126px;text-align:center;font-size:7px;line-height:7.6px;font-weight:500;color:#222}
.field{position:absolute;left:19px;width:105px;height:14px;border:1px solid #ddd;font-size:4.8px;color:#777;line-height:12px;padding-left:5px}
.cta{position:absolute;left:19px;top:124px;width:105px;height:16px;background:var(--blue);color:#fff;font-size:5.2px;font-weight:700;text-align:center;line-height:16px}

.social{width:67px;height:20px;border-radius:3px;color:#fff;font-size:5.8px;font-weight:500;text-align:center;line-height:20px}
.social i{display:inline-block;width:4px;height:4px;background:#fff;border-radius:50%;margin-right:3px;vertical-align:middle;opacity:.9}

.footer-rule{left:156px;top:1073px;width:486px;height:1px;background:var(--rule)}
.footer-brand{left:0;top:1088px;width:798px;text-align:center;font-weight:700;font-size:13px;letter-spacing:1.4px;color:var(--blue)}
.footer-nav{top:1123px;font-size:6.2px;font-weight:600;letter-spacing:.9px;color:#222}
.footer-bar{left:0;top:1169px;width:798px;height:31px;background:var(--blue)}
.copyright{left:156px;top:1181px;font-size:5.8px;color:#fff}
</style>
</head>
<body>
<div class="abs hero" role="img" aria-label="Desk with laptop, keyboard and potted plant in a glass jar"></div>
<header class="abs site-header"></header>
<div class="abs brand">TEACH FORWARD</div>
<nav>
  <span class="abs main-nav" style="left:410px">HOME</span>
  <span class="abs main-nav" style="left:454px">COURSE</span>
  <span class="abs main-nav" style="left:506px">BLOG</span>
  <span class="abs main-nav" style="left:549px">CONSULTING</span>
  <span class="abs main-nav" style="left:618px">ABOUT</span>
</nav>
<div class="abs nav-active"></div>
<div class="abs page-label">BLOG</div>

<article>
  <h2 class="abs post-title" style="top:282px">BLOG ARTICLE SAMPLE</h2>
  <div class="abs post-meta" style="top:302px">May 9, 2018<span>|</span>admin</div>
  <div class="abs post-image" style="top:330px" role="img" aria-label="Teacher writing physics equations on a chalkboard beside a stack of books"></div>
  <p class="abs post-excerpt" style="top:568px">Vestibulum in posuere quam. Donec sollicitudin massa sed orci mattis tincidunt. Fusce a libero vitae tellus molestie tempor. Proin a dui lorem. Aliquam fringilla a ex non aliquet. Etiam efficitur dapibus imperdiet. Nam maximus condimentum mauris eget consectetur. Nam odio lacus, viverra bibendum mauris vitae, scelerisque consequat dui. Duis vel purus imperdiet, ullamcorper ex sit amet, porta elit.</p>
  <div class="abs post-links" style="top:632px">Comments (23) &nbsp;| &nbsp; Date May 09, 2018</div>
</article>
<div class="abs post-rule" style="top:653px"></div>
<article>
  <h2 class="abs post-title" style="top:664px">BLOG ARTICLE SAMPLE</h2>
  <div class="abs post-meta" style="top:684px">May 9, 2018<span>|</span>admin</div>
  <div class="abs post-image" style="top:712px" role="img" aria-label="Teacher writing physics equations on a chalkboard beside a stack of books"></div>
  <p class="abs post-excerpt" style="top:950px">Vestibulum in posuere quam. Donec sollicitudin massa sed orci mattis tincidunt. Fusce a libero vitae tellus molestie tempor. Proin a dui lorem. Aliquam fringilla a ex non aliquet. Etiam efficitur dapibus imperdiet. Nam maximus condimentum mauris eget consectetur. Nam odio lacus, viverra bibendum mauris vitae, scelerisque consequat dui. Duis vel purus imperdiet, ullamcorper ex sit amet, porta elit.</p>
  <div class="abs post-links" style="top:1014px">Comments (23) &nbsp;| &nbsp; Date May 09, 2018</div>
</article>

<aside class="abs signup">
  <div class="bar" style="top:0"></div>
  <h3>Join our community of student around the world helping you to succeed.</h3>
  <div class="field" style="top:65px">Your Name*</div>
  <div class="field" style="top:83px">Email*</div>
  <div class="field" style="top:101px">Phone*</div>
  <div class="cta">GET IT NOW</div>
  <div class="bar thin" style="top:162px"></div>
</aside>

<div class="abs social" style="left:503px;top:506px;background:var(--fb)"><i></i>Faceroom</div>
<div class="abs social" style="left:572px;top:506px;background:var(--tw)"><i></i>Chirper</div>
<div class="abs social" style="left:503px;top:529px;background:var(--pi)"><i></i>Pinwall</div>
<div class="abs social" style="left:572px;top:529px;background:var(--ig)"><i></i>Snapgram</div>
<div class="abs social" style="left:503px;top:553px;background:var(--gp)"><i></i>Circles+</div>
<div class="abs social" style="left:572px;top:553px;background:var(--li)"><i></i>WorkLink</div>
<div class="abs social" style="left:503px;top:576px;background:var(--yt)"><i></i>VidTube</div>
<div class="abs social" style="left:572px;top:576px;background:var(--rss)"><i></i>RSS Feed</div>

<div class="abs footer-rule"></div>
<div class="abs footer-brand">TEACH FORWARD</div>
<nav>
  <span class="abs footer-nav" style="left:260px">HOME</span>
  <span class="abs footer-nav" style="left:315px">COURSE</span>
  <span class="abs footer-nav" style="left:379px">BLOG</span>
  <span class="abs footer-nav" style="left:433px">CONSULTING</span>
  <span class="abs footer-nav" style="left:514px">ABOUT</span>
</nav>
<footer class="abs footer-bar"></footer>
<div class="abs copyright">Copyright 2018 <b>Teach Forward</b></div>
</body>
</html>
```